Political sign design, fonts colors and layout

I am running for Town Council.

My message is done, and *a draft is attached* with the text we wish to use. It says "Elect Dana Velloway" etc. In Maroon and White. I am not a designer, but this is somewhat close to what we are looking for.

I need help with colors and fonts, layout, spacing, and general cleanup.

I'm attaching the town high school logo:

- "B" for Brockmere: with black and white outlines on the fonts
- we want to incorporate the black and white on the fonts
- for the entire text, parts of the text, or best would be a mix

This is for signs printed and placed all over my town.

We need two versions

1. square, 4' by 4' version
2. 36" by 24" version

The smaller version will drop the three bullet pointed text, but otherwise can be identical.

The sign can only use 3 printed colors (due to printing costs.)

1. maroon,
2. white,
3. black.

The maroon should match the maroon from the high school logo attached, which I believe I did in the draft.

We also like the white border around the outside, like in the "scoreboard" design attached.

Thanks for your attention, wish me luck.

Dana

Target Market(s)

SIgns, Political market

Industry/Entity Type

Political

Font styles to use
Sans Serif
Other font styles liked:
• Arial Black, Sans Serif Bold

Requirements
Must have
• maroon background, white font.
• - black borders around fonts where appropriate
• - great spacing
• - great typeface usage
• - clean and crisp political sign, visible while driving.
• - my name "Dana Velloway" much larger like the draft, or the appropriate additional size
• - two versions, one square, and one 36" / 24"
Nice to have
• - nice borders
• - dress it up a bit, using italics and bold fonts, without making it flashy or busy.
Should not have
• Must be easily readable from a car, except for "Paid for by Friends of Dana Velloway" which can be tiny.
• Colors are noted in the description, the "Brockmere Maroon" as the background, white font, and some use of black.

```html
<!DOCTYPE html>
<html lang="en">
<head>
<meta charset="UTF-8">
<title>Elect Dana Velloway – Yard Sign</title>
<link rel="stylesheet" href="https://fonts.googleapis.com/css2?family=Raleway:wght@400;800;900&display=swap">
<style>
  :root {
    --maroon: #781b30;
    --white: #ffffff;
    --black: #111111;
    --rule: 6px;
  }
  * { margin: 0; padding: 0; box-sizing: border-box; }
  html, body { width: 1200px; height: 800px; overflow: hidden; background: var(--white); }
  body { font-family: "Raleway", Arial, sans-serif; color: var(--white); }

  .sign { position: relative; width: 1200px; height: 800px; background: var(--white); }

  .field {
    position: absolute; left: 20px; width: 1160px; background: var(--maroon);
  }
  .field--top { top: 20px; height: 228px; }
  .field--bottom { top: 350px; height: 428px; }

  .line {
    position: absolute; left: 0; right: 0; text-align: center; white-space: nowrap;
    transform: translateY(-50%); line-height: 1;
  }

  .outlined {
    -webkit-text-stroke: 4px var(--black);
    paint-order: stroke fill;
  }
  .outlined--thin {
    -webkit-text-stroke: 3px var(--black);
    paint-order: stroke fill;
  }

  .ruled {
    position: absolute; left: 0; right: 0; display: flex; align-items: center;
    transform: translateY(-50%);
  }
  .ruled::before, .ruled::after {
    content: ""; flex: 1; height: var(--rule); background: var(--white);
  }
  .ruled span { line-height: 1; white-space: nowrap; }

  .slogan { top: 92px; font-size: 75px; font-weight: 800; letter-spacing: -0.5px; }
  .elect { top: 188px; }
  .elect span { font-size: 70px; font-weight: 900; padding: 0 30px; }

  .band-name {
    position: absolute; left: 0; top: 248px; width: 1200px; height: 102px;
  }
  .candidate {
    top: 53px; color: var(--maroon); font-size: 106px; font-weight: 900;
  }

  .tagline { top: 52px; font-size: 62px; font-weight: 800; }
  .website { top: 98px; font-size: 28px; font-weight: 900; letter-spacing: 0.5px; }

  .issue span { font-size: 35px; font-weight: 800; }
  .issue--taxes { top: 157px; }
  .issue--taxes span { padding: 0 20px; }
  .issue--government { top: 201px; }
  .issue--government span { padding: 0 24px; }
  .issue--neighborhoods { top: 245px; }
  .issue--neighborhoods span { padding: 0 24px; }

  .vote { top: 323px; font-size: 63px; font-weight: 800; }
  .disclaimer { top: 393px; font-size: 26px; font-weight: 400; }
</style>
</head>
<body>
  <main class="sign">
    <section class="field field--top">
      <p class="line slogan outlined">Take Back Our Town</p>
      <div class="ruled elect"><span class="outlined">ELECT</span></div>
    </section>

    <section class="band-name">
      <h1 class="line candidate outlined">DANA VELLOWAY</h1>
    </section>

    <section class="field field--bottom">
      <p class="line tagline outlined">Fighting for Brockmere</p>
      <p class="line website">www.velloway4council.com</p>
      <div class="ruled issue issue--taxes"><span class="outlined--thin">Stop High Taxes</span></div>
      <div class="ruled issue issue--government"><span class="outlined--thin">Clean up Our Government</span></div>
      <div class="ruled issue issue--neighborhoods"><span class="outlined--thin">Preserve Our Neighborhoods</span></div>
      <p class="line vote outlined">Vote Nov. 8th "Row A"</p>
      <p class="line disclaimer">Paid for by Friends of Dana</p>
    </section>
  </main>
</body>
</html>
```